"Psychic / Tarot Card Reader / Healer Needs a Web Page Design

We need a web page design for company that does psychic / tarot card readings / healings etc.
It currently has 6 different tabs which include: Home, testimonials, service, certificates, contact us plus a shop where if people want to they can purchase services on line.
Should be mystical / magic like yet simple.
Will upload a copy of the current logo for the business.
It's name is Lunar Hollow.

Target Market(s)

spiritual

Industry/Entity Type

It Company

Number of Pages Required

5+ page

```html
<!DOCTYPE html>
<html lang="en">
<head>
<meta charset="utf-8">
<title>Lunar Hollow</title>
<link rel="stylesheet" href="https://fonts.googleapis.com/css2?family=Roboto:wght@300;400;500;700;900&display=swap">
<style>
:root{
  --purple:#92278f;
  --purple-dark:#7a1f78;
  --teal:#2b9fb8;
  --teal-dark:#1f7f98;
  --ink:#222;
  --text:#555;
  --muted:#777;
  --grey-bg:#f3f3f3;
  --line:#e2e2e2;
  --contact-bg:#c9e4ef;
  --footer:#232323;
}
*{box-sizing:border-box;margin:0;padding:0}
html,body{width:1200px;height:5172px;overflow:hidden}
body{font-family:'Roboto',Arial,sans-serif;color:var(--text);background:#fff;font-size:13px;line-height:1.6}
.wrap{width:1076px;margin:0 auto;position:relative}

/* header */
.site-header{height:93px;background:#fff;display:flex;align-items:center;justify-content:space-between;padding:0 40px 0 30px;box-shadow:0 1px 3px rgba(0,0,0,.08);position:relative;z-index:2}
.brand{display:flex;align-items:center;gap:10px;font-size:22px;font-weight:500;color:var(--purple)}
.brand-dot{width:14px;height:14px;border-radius:50%;background:var(--purple)}
.main-nav{display:flex;gap:30px;font-size:14px;color:#444}
.main-nav a{text-decoration:none;color:inherit;padding-bottom:6px}
.main-nav a.active{color:var(--purple);border-bottom:2px solid var(--purple)}

/* hero */
.hero{height:527px;position:relative;border-bottom:5px solid var(--purple);
  background:radial-gradient(circle at 22% 45%,#5fd3d0 0%,#2a8d9a 20%,transparent 45%),
             radial-gradient(circle at 60% 50%,#c6553c 0%,#6e2a3a 25%,transparent 55%),
             linear-gradient(90deg,#1d4e64,#3a2440 50%,#1a1530);}
.hero-arrow{position:absolute;top:50%;width:14px;height:14px;border-top:2px solid #fff;border-left:2px solid #fff;opacity:.8}
.hero-arrow.prev{left:18px;transform:rotate(-45deg)}
.hero-arrow.next{right:18px;transform:rotate(135deg)}

/* section heads */
.section-title{font-size:40px;font-weight:700;color:var(--ink);text-align:center;letter-spacing:.5px;line-height:1.1}
.title-dot{display:block;width:12px;height:12px;border-radius:50%;background:var(--purple);margin:18px auto 16px}
.section-lead{width:500px;margin:0 auto;text-align:center;font-size:13px;color:var(--text)}

/* services */
.services{height:645px;padding-top:115px}
.service-grid{display:grid;grid-template-columns:repeat(3,1fr);column-gap:60px;row-gap:50px;margin-top:60px}
.service{display:flex;gap:20px}
.service-icon{flex:none;width:48px;height:48px;border-radius:50%;border:1px solid var(--line);display:flex;align-items:center;justify-content:center}
.service h3{font-size:16px;font-weight:500;color:var(--ink);margin-bottom:4px}
.service p{font-size:13px;width:230px}

/* portfolio */
.portfolio{height:811px;background:var(--grey-bg);padding-top:110px}
.filters{display:flex;justify-content:center;margin-top:40px}
.filters span{padding:6px 14px;font-size:12px;background:#e6e6e6;color:#444}
.filters span.active{background:var(--purple);color:#fff}
.works{display:grid;grid-template-columns:repeat(4,250px);gap:27px 25px;margin-top:36px}
.work{height:165px}
.w1{background:linear-gradient(135deg,#b8b2a6,#7c6c52)}
.w2{background:radial-gradient(circle,#e1b43c 10%,#1f4aa8 60%)}
.w3{background:radial-gradient(circle,#d9a33a 15%,#0d2d8a 65%)}
.w4{background:radial-gradient(circle,#f2c85a 10%,#c1622a 70%)}
.w5{background:radial-gradient(circle,#ffe26a 15%,#c23a12 70%)}
.w6{background:radial-gradient(circle at 50% 60%,#fff0a0 5%,#d77a18 45%,#4a1c10)}
.w7{background:linear-gradient(135deg,#2f8fae,#a8c7bd 55%,#2e5c8a)}
.w8{background:radial-gradient(circle,#2e80d8 15%,#0b1a55 70%)}

/* about */
.about{height:811px;padding-top:125px}
.about-sub{text-align:center;font-size:12px;margin-top:-2px}
.about-cols{display:grid;grid-template-columns:520px 520px;column-gap:36px;margin-top:48px}
.col-title{font-size:20px;font-weight:500;color:var(--ink);padding-bottom:14px;border-bottom:1px solid var(--line);margin-bottom:18px}
.about p{font-size:13px;margin-bottom:12px}
.video{height:290px;margin-top:8px;position:relative;background:linear-gradient(180deg,#e9e3d6 0%,#f1ecdf 60%,#cfc6b4 100%)}
.video-bar{position:absolute;left:10px;right:10px;bottom:10px;height:34px;display:flex;align-items:center;gap:10px}
.video-play{width:48px;height:34px;background:rgba(0,0,0,.8);display:flex;align-items:center;justify-content:center}
.video-track{flex:1;height:10px;background:rgba(0,0,0,.7)}
.checks{display:grid;grid-template-columns:1fr 1fr;gap:4px;margin:4px 0 20px}
.checks li{list-style:none;display:flex;align-items:center;gap:8px;font-size:13px}
.tick{width:13px;height:13px;background:var(--purple);display:inline-flex;align-items:center;justify-content:center}
.btn{display:inline-block;background:var(--purple);color:#fff;font-size:12px;font-weight:500;padding:8px 14px;border:0}

/* pricing */
.pricing{height:844px;padding-top:97px}
.plans{display:grid;grid-template-columns:345px 335px 345px;gap:0 25px;margin-top:150px;align-items:start}
.plan{position:relative;background:#fff;border:1px solid #ececec;box-shadow:0 1px 4px rgba(0,0,0,.06);text-align:center;height:420px}
.plan-head{height:112px;background:#eeeeee;padding-top:68px;font-size:22px;font-weight:700;color:var(--ink);border-bottom:2px solid #ddd}
.price{position:absolute;top:-55px;left:50%;transform:translateX(-50%);width:100px;height:100px;border-radius:50%;background:var(--purple);border:5px solid #fff;color:#fff;display:flex;flex-direction:column;align-items:center;justify-content:center;box-shadow:0 0 0 1px #ddd}
.price b{font-size:24px;line-height:1}
.price small{font-size:11px}
.plan ul{list-style:none;padding-top:22px}
.plan li{font-size:13px;color:#333;padding:9px 0}
.plan .btn{margin-top:14px}
.plan.featured{background:var(--purple);height:425px;border:none}
.plan.featured .plan-head{background:var(--teal);color:#fff;border-bottom:none}
.plan.featured li{color:#fff}

/* testimonial */
.testimonial{height:345px;position:relative;text-align:center;color:#fff;padding-top:62px;
  background:linear-gradient(180deg,rgba(20,22,32,.85),rgba(20,22,32,.85)),linear-gradient(90deg,#5a4a44,#3a3a4a,#5b4b3c,#40404e)}
.avatar{width:90px;height:90px;border-radius:50%;border:3px solid #fff;margin:0 auto 12px;background:linear-gradient(135deg,#c79a7a,#7a4f3a)}
.testimonial h4{font-size:20px;font-weight:500}
.testimonial .role{font-size:11px;color:#ccc;margin-bottom:10px}
.testimonial .quote{width:720px;margin:0 auto;font-size:13px;font-weight:700}
.t-nav{display:flex;gap:4px;justify-content:center;margin-top:14px}
.t-nav span{width:22px;height:24px;background:var(--purple);display:flex;align-items:center;justify-content:center}

/* get in touch */
.touch{height:310px;background:linear-gradient(180deg,var(--teal-dark),var(--teal) 60%,#35b2c4);text-align:center;color:#fff;padding-top:90px}
.touch .section-title{color:#fff}
.touch .title-dot{background:var(--purple);border:3px solid #fff;width:16px;height:16px;position:relative}
.touch .title-dot::before,.touch .title-dot::after{content:"";position:absolute;top:5px;width:70px;height:1px;background:rgba(255,255,255,.6)}
.touch .title-dot::before{right:18px}.touch .title-dot::after{left:18px}
.touch .section-lead{color:#fff;font-weight:700;width:580px}

/* contact */
.contact{height:614px;background:var(--contact-bg);padding-top:50px}
.contact-box{margin-left:738px;width:338px;height:535px;background:#f4f9fb;padding:20px 18px}
.contact-box h3{font-size:22px;font-weight:500;color:var(--ink)}
.contact-box .org{font-size:13px;color:var(--ink);margin:6px 0 14px}
.field{height:32px;border:1px solid #ccd8de;background:#fff;margin-bottom:12px;font-size:12px;padding:7px 10px;color:#666}
.field.message{height:160px}
.contact-box .btn{margin-top:4px}

/* footer */
.site-footer{height:179px;background:var(--footer);color:#fff;display:flex;align-items:center;justify-content:space-between;padding:0 62px}
.site-footer p{font-size:13px;font-weight:700}
.social{display:flex;gap:16px}
.social span{width:11px;height:11px;background:#bbb;border-radius:2px}
</style>
</head>
<body>

<header class="site-header">
  <div class="brand"><span class="brand-dot"></span>Lunar Hollow</div>
  <nav class="main-nav">
    <a class="active" href="#">Home</a><a href="#">Services</a><a href="#">Portfolio</a><a href="#">Testimonials</a><a href="#">About Us</a><a href="#">Shop</a><a href="#">Contact Us</a>
  </nav>
</header>

<section class="hero" role="img" aria-label="Cosmic banner: zodiac wheel in a teal nebula beside a glowing starry lion constellation">
  <span class="hero-arrow prev"></span><span class="hero-arrow next"></span>
</section>

<section class="services">
  <div class="wrap">
    <h2 class="section-title">OUR SERVICES</h2>
    <span class="title-dot"></span>
    <p class="section-lead">Lorem ipsum dolor sit amet, consectetur adipisicing elit, sed do eiusmod tempor incididunt ut et dolore magna aliqua. Ut enim ad minim veniam</p>
    <div class="service-grid">
      <div class="service"><span class="service-icon"><svg width="20" height="20" viewBox="0 0 20 20"><polyline points="2,16 8,9 12,12 18,4" fill="none" stroke="#92278f" stroke-width="2"/></svg></span><div><h3>Horoscopes</h3><p>Backed by some of the biggest names in the industry, Nimbus OS is an open platform that fosters greater</p></div></div>
      <div class="service"><span class="service-icon"><svg width="20" height="20" viewBox="0 0 20 20"><path d="M2 6l8-3 8 3-8 3z M2 11l8 3 8-3" fill="none" stroke="#92278f" stroke-width="2"/></svg></span><div><h3>Tarrot card reading</h3><p>Backed by some of the biggest names in the industry, Nimbus OS is an open platform that fosters greater</p></div></div>
      <div class="service"><span class="service-icon"><svg width="20" height="20" viewBox="0 0 20 20"><circle cx="10" cy="10" r="7" fill="none" stroke="#92278f" stroke-width="2"/><circle cx="10" cy="10" r="2" fill="#92278f"/></svg></span><div><h3>Psychic</h3><p>Backed by some of the biggest names in the industry, Nimbus OS is an open platform that fosters greater</p></div></div>
      <div class="service"><span class="service-icon"><svg width="20" height="20" viewBox="0 0 20 20"><rect x="3" y="10" width="3" height="7" fill="#92278f"/><rect x="8.5" y="6" width="3" height="11" fill="#92278f"/><rect x="14" y="3" width="3" height="14" fill="#92278f"/></svg></span><div><h3>Healings</h3><p>Backed by some of the biggest names in the industry, Nimbus OS is an open platform that fosters greater</p></div></div>
      <div class="service"><span class="service-icon"><svg width="20" height="20" viewBox="0 0 20 20"><rect x="3" y="3" width="14" height="14" fill="none" stroke="#92278f" stroke-width="2"/><line x1="3" y1="10" x2="17" y2="10" stroke="#92278f" stroke-width="2"/></svg></span><div><h3>Kundali</h3><p>Backed by some of the biggest names in the industry, Nimbus OS is an open platform that fosters greater</p></div></div>
      <div class="service"><span class="service-icon"><svg width="20" height="20" viewBox="0 0 20 20"><circle cx="10" cy="10" r="7" fill="none" stroke="#92278f" stroke-width="2"/><polyline points="10,5 10,10 14,12" fill="none" stroke="#92278f" stroke-width="2"/></svg></span><div><h3>Predictions</h3><p>Backed by some of the biggest names in the industry, Nimbus OS is an open platform that fosters greater</p></div></div>
    </div>
  </div>
</section>

<section class="portfolio">
  <div class="wrap">
    <h2 class="section-title">PORTFOLIO</h2>
    <span class="title-dot"></span>
    <p class="section-lead">Lorem ipsum dolor sit amet, consectetur adipisicing elit, sed do eiusmod tempor incididunt ut et dolore magna aliqua. Ut enim ad minim veniam</p>
    <div class="filters"><span class="active">All Works</span><span>Creative</span><span>Corporate</span><span>Portfolio</span></div>
    <div class="works">
      <div class="work w1" role="img" aria-label="Tarot cards fanned on a table"></div>
      <div class="work w2" role="img" aria-label="Blue and gold zodiac wheel"></div>
      <div class="work w3" role="img" aria-label="Ornate astrological clock face"></div>
      <div class="work w4" role="img" aria-label="Golden zodiac dial on orange"></div>
      <div class="work w5" role="img" aria-label="Blazing sun"></div>
      <div class="work w6" role="img" aria-label="Meditating figure in glowing light"></div>
      <div class="work w7" role="img" aria-label="Astrology chart over a sky map"></div>
      <div class="work w8" role="img" aria-label="Blue zodiac circle of signs"></div>
    </div>
  </div>
</section>

<section class="about">
  <div class="wrap">
    <h2 class="section-title">ABOUT US</h2>
    <span class="title-dot"></span>
    <p class="about-sub">All About us</p>
    <div class="about-cols">
      <div>
        <h3 class="col-title">Video Intro</h3>
        <p>industry's standard dummy text ever since the 1500s, when an unknown printer took a galley of type and scrambled it to make a type specimen book.</p>
        <p>Lorem Ipsum has been the industry's standard dummy text ever since the 1500s, when an unknown printer took a galley of type and scrambled it to make a type specimen book.</p>
        <div class="video" role="img" aria-label="Intro video still: cartoon character in a colourful city scene">
          <div class="video-bar">
            <span class="video-play"><svg width="14" height="14" viewBox="0 0 14 14"><polygon points="3,1 13,7 3,13" fill="#fff"/></svg></span>
            <span class="video-track"></span>
          </div>
        </div>
      </div>
      <div>
        <h3 class="col-title">Lunar Hollow</h3>
        <p>industry's standard dummy text ever since the 1500s, when an unknown printer took a galley of type and scrambled it to make a type specimen book.</p>
        <p>Lorem Ipsum has been the industry's standard dummy text ever since the 1500s, when an unknown printer took a galley of type and scrambled it to make a type specimen book.</p>
        <ul class="checks">
          <li><span class="tick"><svg width="9" height="9" viewBox="0 0 9 9"><polyline points="1,5 3.5,7 8,1.5" fill="none" stroke="#fff" stroke-width="1.6"/></svg></span>Ipsum is simply dummy</li>
          <li><span class="tick"><svg width="9" height="9" viewBox="0 0 9 9"><polyline points="1,5 3.5,7 8,1.5" fill="none" stroke="#fff" stroke-width="1.6"/></svg></span>The printing and typesetting</li>
          <li><span class="tick"><svg width="9" height="9" viewBox="0 0 9 9"><polyline points="1,5 3.5,7 8,1.5" fill="none" stroke="#fff" stroke-width="1.6"/></svg></span>When an unknown</li>
          <li><span class="tick"><svg width="9" height="9" viewBox="0 0 9 9"><polyline points="1,5 3.5,7 8,1.5" fill="none" stroke="#fff" stroke-width="1.6"/></svg></span>Lorem Ipsum has been</li>
        </ul>
        <span class="btn">Learn More</span>
      </div>
    </div>
  </div>
</section>

<section class="pricing">
  <div class="wrap">
    <h2 class="section-title">PRICING TABLE</h2>
    <span class="title-dot"></span>
    <p class="section-lead">Lorem ipsum dolor sit amet, consectetur adipisicing elit, sed do eiusmod tempor incididunt ut et dolore magna aliqua. Ut enim ad minim veniam</p>
    <div class="plans">
      <div class="plan">
        <div class="price"><b>Rs39</b><small>per month</small></div>
        <div class="plan-head">STARTER</div>
        <ul><li>Horoscopes</li><li>Kundali</li></ul>
        <span class="btn">ORDER NOW</span>
      </div>
      <div class="plan featured">
        <div class="price"><b>Rs69</b><small>per month</small></div>
        <div class="plan-head">BUSINESS</div>
        <ul><li>Horoscopes</li><li>Kundali</li><li>Tarrot Card reading</li></ul>
      </div>
      <div class="plan">
        <div class="price"><b>Rs199</b><small>per month</small></div>
        <div class="plan-head">ULTRA</div>
        <ul><li>Horoscopes</li><li>Kundali</li><li>Tarrot Card reading</li><li>Healing</li><li>Physic</li></ul>
        <span class="btn">ORDER NOW</span>
      </div>
    </div>
  </div>
</section>

<section class="testimonial" role="img" aria-label="Darkened backdrop of many customer portraits">
  <div class="avatar" role="img" aria-label="Customer portrait"></div>
  <h4>Marion T. Vale</h4>
  <p class="role">Treatment, storage, and disposal (TSD) worker</p>
  <p class="quote">Lorem ipsum dolor sit amet, consectetur adipisicing elit, sed do eiusmod tempor incididunt ut et dolore magna aliqua. Ut enim ad minim veniam</p>
  <div class="t-nav">
    <span><svg width="8" height="10" viewBox="0 0 8 10"><polyline points="6,1 2,5 6,9" fill="none" stroke="#fff" stroke-width="1.6"/></svg></span>
    <span><svg width="8" height="10" viewBox="0 0 8 10"><polyline points="2,1 6,5 2,9" fill="none" stroke="#fff" stroke-width="1.6"/></svg></span>
  </div>
</section>

<section class="touch">
  <h2 class="section-title">GET IN TOUCH</h2>
  <span class="title-dot"></span>
  <p class="section-lead">Lorem ipsum dolor sit amet, consectetur adipisicing elit, sed do eiusmod tempor incididunt ut et dolore magna aliqua. Ut enim ad minim veniam</p>
</section>

<section class="contact">
  <div class="wrap">
    <div class="contact-box">
      <h3>Contact Info</h3>
      <p class="org">Lunar Hollow</p>
      <div class="field">Name</div>
      <div class="field">Email</div>
      <div class="field">Subject</div>
      <div class="field message">Message</div>
      <span class="btn">Send Message</span>
    </div>
  </div>
</section>

<footer class="site-footer">
  <p>© 2017 Lunar Hollow.</p>
  <div class="social"><span></span><span></span><span></span><span></span><span></span><span></span><span></span><span></span><span></span><span></span></div>
</footer>

</body>
</html>
```